Website for Party

Design a new website for PrismGatherings.com
We have attached the new logos and please look at the website, and our facebook page: facebook.com/prismgatherings for inspiration
Updates

Hi Guys, please be original with all designs and images otherwise the design will be eliminated Thank you

some of your designs have too much happening in them, others make it clear that the designer has not yet read the brief fully

Please everyone be original!

```html
<!DOCTYPE html>
<html lang="en">
<head>
<meta charset="utf-8">
<title>Prism Gatherings</title>
<link rel="stylesheet" href="https://fonts.googleapis.com/css2?family=Nunito:wght@400;700;800&family=Nunito+Sans:wght@400;700&display=swap">
<style>
  :root {
    --page-bg: #ffffff;
    --header-bg: #2b2b2b;
    --logo-bg: #000000;
    --panel-bg: #1c1c1c;
    --footer-bg: #454545;
    --text-light: #ffffff;
    --text-soft: #dddddd;
    --text-muted: #9a9a9a;
    --icon-grey: #8a8a8a;
    --social-grey: #cfcfcf;
    --hero-light: #e6d3f2;
    --hero-mid: #b77fd9;
    --hero-deep: #6a1f9c;
  }
  * { margin: 0; padding: 0; box-sizing: border-box; }
  html, body { width: 1200px; height: 1000px; overflow: hidden; background: var(--page-bg); }
  body { position: relative; font-family: "Nunito Sans", Verdana, sans-serif; }

  .site-header {
    position: absolute; left: 0; top: 216px; width: 1200px; height: 89px;
    background: var(--header-bg);
  }
  .brand {
    position: absolute; left: 24px; top: 16px; width: 71px; height: 61px;
    background: var(--logo-bg); display: flex; align-items: center; justify-content: center;
    color: var(--text-light); font-family: "Nunito", sans-serif; font-weight: 700; font-size: 17px;
  }
  .main-nav { position: absolute; left: 180px; top: 49px; display: flex; gap: 0; }
  .main-nav a {
    font-family: "Nunito Sans", Verdana, sans-serif; font-size: 11px; color: var(--text-muted);
    text-decoration: none; margin-right: 40px;
  }
  .main-nav a.is-active { color: var(--text-light); font-weight: 700; }

  .call-box { position: absolute; left: 1047px; top: 24px; }
  .call-icon { position: absolute; left: 0; top: 4px; width: 29px; height: 29px; }
  .call-title {
    position: absolute; left: 41px; top: -2px; white-space: nowrap;
    font-family: "Nunito", sans-serif; font-weight: 700; font-size: 18px; color: var(--text-light);
  }
  .call-number {
    position: absolute; left: 41px; top: 26px; white-space: nowrap;
    font-size: 11px; color: var(--text-muted);
  }

  .hero {
    position: absolute; left: 0; top: 305px; width: 1200px; height: 463px;
    background:
      radial-gradient(ellipse at 55% 45%, var(--hero-light) 0%, rgba(230,211,242,0) 55%),
      linear-gradient(90deg, #cdb3e0 0%, #c9a3e6 45%, var(--hero-mid) 75%, var(--hero-deep) 100%);
  }
  .hero-panel {
    position: absolute; left: 0; top: 54px; width: 462px; height: 364px;
    background: var(--panel-bg);
  }
  .hero-title {
    position: absolute; left: 27px; top: 84px;
    font-family: "Nunito", sans-serif; font-weight: 800; font-size: 28px; color: var(--text-light);
  }
  .hero-text {
    position: absolute; left: 27px; top: 128px; width: 410px;
    font-size: 11px; line-height: 19px; color: var(--text-soft);
  }
  .hero-crumb {
    position: absolute; right: 13px; bottom: 6px;
    font-size: 10px; font-weight: 700; color: var(--text-light);
  }

  .site-footer {
    position: absolute; left: 0; top: 768px; width: 1200px; height: 25px;
    background: var(--footer-bg);
  }
  .social-links { position: absolute; left: 24px; top: 9px; display: flex; gap: 1px; }
  .social-dot { width: 19px; height: 19px; border-radius: 50%; background: var(--social-grey); }
  .site-footer { overflow: hidden; }
  .credit {
    position: absolute; right: 10px; top: 11px; font-size: 10px; color: var(--text-muted);
  }
  .credit strong { color: var(--text-light); }
</style>
</head>
<body>
  <header class="site-header">
    <div class="brand">Prism</div>
    <nav class="main-nav">
      <a class="is-active" href="#">Home</a>
      <a href="#">About Us</a>
      <a href="#">Order Tickets</a>
      <a href="#">Contact</a>
    </nav>
    <div class="call-box">
      <svg class="call-icon" viewBox="0 0 29 29" aria-hidden="true">
        <circle cx="14.5" cy="14.5" r="14" fill="var(--icon-grey)"/>
        <path d="M11 8.5c-1.6 1-2 3.2-.8 6.2 1.2 3 3.2 5.3 5.6 6 1.2.3 2.2 0 2.8-.7l-2-2.6-1.6.8c-1-.6-2.2-2.4-2.6-3.8l1.4-1.1-1.2-3.1z" fill="#2b2b2b"/>
      </svg>
      <div class="call-title">Call Us Now</div>
      <div class="call-number">+11 400555172</div>
    </div>
  </header>

  <section class="hero" role="img" aria-label="Purple-lit concert crowd with stage lights and raised hands">
    <div class="hero-panel">
      <h1 class="hero-title">Exclusive Party</h1>
      <p class="hero-text">Here at Prism, webring the most talented artists to spectacular venues of the Greater NYC area for you to enjoy!</p>
      <span class="hero-crumb">Home</span>
    </div>
  </section>

  <footer class="site-footer">
    <div class="social-links">
      <span class="social-dot"></span>
      <span class="social-dot"></span>
      <span class="social-dot"></span>
      <span class="social-dot"></span>
    </div>
    <div class="credit">Powered by <strong>qrs</strong></div>
  </footer>
</body>
</html>
```